Tide Harbor Finance Business Cards

Looking for a business card for a new mortgage broking business. Name of the business is Tide Harbor Finance. Purpose of the business is to build trust and strong relationships with clients to then assist them with your mortgage lending needs. Most relationships within the business start off as an enquiry, and then can evolve into a 10+ year relationship, servicing clients from purchasing a new home to then upgrading for their family and even then assisting their children with their first home purchase. Business card should communicate financial security and trust.

Target Market(s)

Targeting professional clients who are looking to build a relationship with a knowledgeable mortgage professional

Industry/Entity Type

Finance - Home Loans

Contact Information for Business Card

Peter Colburn, Director, mobile: 0427 903186, email:peter@tideharborfinance.com.au, website: www.tideharborfinance.com.au

Font styles to use
Sans Serif

Requirements
Must have
• On the front: Must have company logo, contact details as above. On the back: slogan, 'Steady choices, secure futures', plus listing services offered: home loans, investment loans, first home buyers, refinancing, car finance

```html
<!DOCTYPE html>
<html lang="en">
<head>
<meta charset="utf-8">
<title>Tide Harbor Finance Business Cards</title>
<link rel="stylesheet" href="https://fonts.googleapis.com/css2?family=Montserrat:wght@700&family=Roboto:wght@400;500&display=swap">
<style>
  :root {
    --navy: #0d4f7a;
    --ink: #1f4766;
    --gold: #f2a21d;
    --paper: #ffffff;
    --stage: #e9ecef;
    --text: #3a3f45;
  }
  * { box-sizing: border-box; margin: 0; padding: 0; }
  html, body { width: 1200px; height: 900px; overflow: hidden; }
  body {
    background: var(--stage);
    font-family: "Roboto", Arial, sans-serif;
    position: relative;
  }
  .card {
    position: absolute;
    width: 560px;
    height: 342px;
    border-radius: 4px;
    box-shadow: 0 6px 18px rgba(0,0,0,0.18);
  }
  .card--back { left: 50px; top: 80px; background: var(--navy); color: #fff; }
  .card--front { left: 590px; top: 478px; background: var(--paper); }

  .brand {
    display: flex;
    align-items: center;
    gap: 12px;
    font-family: "Roboto", Arial, sans-serif;
    font-weight: 500;
    text-transform: uppercase;
    line-height: 1.02;
  }
  .brand__mark { width: 22px; height: 22px; border-radius: 4px; flex: none; }
  .brand__name { font-size: 30px; letter-spacing: 0.5px; }

  .card--back .brand { position: absolute; left: 46px; top: 118px; }
  .card--back .brand__mark { background: var(--gold); }
  .card--back .brand__name { color: #fff; }

  .slogan {
    position: absolute;
    left: 46px;
    top: 236px;
    color: var(--gold);
    font-size: 13.5px;
    letter-spacing: 0.6px;
    text-transform: uppercase;
  }

  .services {
    position: absolute;
    left: 335px;
    top: 96px;
    list-style: none;
  }
  .services li {
    font-size: 17px;
    line-height: 28px;
    display: flex;
    align-items: center;
    gap: 9px;
  }
  .services li::before {
    content: "";
    width: 7px; height: 7px;
    border-radius: 50%;
    background: var(--gold);
  }

  .card--front .brand { position: absolute; right: 40px; top: 40px; }
  .card--front .brand__mark { background: var(--gold); }
  .card--front .brand__name { color: var(--ink); font-size: 26px; }

  .person { position: absolute; left: 44px; top: 178px; }
  .person__name {
    font-family: "Montserrat", Arial, sans-serif;
    font-weight: 700;
    font-size: 18px;
    color: var(--ink);
    letter-spacing: 0.3px;
    text-transform: uppercase;
  }
  .person__role { color: var(--gold); font-size: 16px; margin-top: 2px; }

  .contacts { position: absolute; left: 44px; top: 244px; list-style: none; }
  .contacts li {
    display: flex;
    align-items: center;
    gap: 12px;
    font-size: 15.5px;
    color: var(--text);
    line-height: 25px;
  }
  .contacts svg { width: 16px; height: 16px; flex: none; fill: var(--ink); }
</style>
</head>
<body>
  <section class="card card--back" aria-label="Card back">
    <div class="brand">
      <span class="brand__mark"></span>
      <span class="brand__name">Tide Harbor<br>Finance</span>
    </div>
    <p class="slogan">Steady choices, secure futures</p>
    <ul class="services">
      <li>Home Loans</li>
      <li>Investment Loans</li>
      <li>First Home Buyers</li>
      <li>Refinancing</li>
      <li>Car Finance</li>
    </ul>
  </section>

  <section class="card card--front" aria-label="Card front">
    <div class="brand">
      <span class="brand__mark"></span>
      <span class="brand__name">Tide Harbor<br>Finance</span>
    </div>
    <div class="person">
      <p class="person__name">Peter Colburn</p>
      <p class="person__role">Director</p>
    </div>
    <ul class="contacts">
      <li>
        <svg viewBox="0 0 16 16" aria-hidden="true"><path d="M4 0h8a1.5 1.5 0 0 1 1.5 1.5v13A1.5 1.5 0 0 1 12 16H4a1.5 1.5 0 0 1-1.5-1.5v-13A1.5 1.5 0 0 1 4 0zm0 2v10.5h8V2zm4 11.2a.9.9 0 1 0 0 1.8.9.9 0 0 0 0-1.8z"/></svg>
        0427 903186
      </li>
      <li>
        <svg viewBox="0 0 16 16" aria-hidden="true"><path d="M0 3h16v1.2L8 9 0 4.2zm0 2.6 8 4.8 8-4.8V13H0z"/></svg>
        peter@tideharborfinance.com.au
      </li>
      <li>
        <svg viewBox="0 0 16 16" aria-hidden="true"><circle cx="8" cy="8" r="8"/><path d="M3 6c2-1 3 0 3 1.5S5 10 6 12M10 2.5c0 2 2 2 3 3M10 14c0-2 1-3 2.5-3" stroke="#fff" stroke-width="1.2" fill="none"/></svg>
        www.tideharborfinance.com.au
      </li>
    </ul>
  </section>
</body>
</html>
```